Vorna Electric Construction We Light It Up!

We have an up coming meeting with a developer and general contractor. This card must bring out the best in my business. My business is an up and coming MDBE certified electrical contactor. I need a very powerful card to represent me business that we be bold and represent what I am about. WE LIGHT IT UP!

Target Market(s)

General Contractors, developers and property owners

Industry/Entity Type

Electrical

Contact Information for Business Card

great card that really brings out my bussiness

Colors
0355a3
3276b5
0393ce
34a6d7

Requirements
Must have
• Great design
Nice to have
• very different and noticeable card
Should not have
• open to anything

```html
<!DOCTYPE html>
<html lang="en">
<head>
<meta charset="utf-8">
<title>Vorna Electric Construction – Business Card</title>
<link href="https://fonts.googleapis.com/css2?family=Source+Sans+3:wght@400;600;700&display=swap" rel="stylesheet">
<style>
  :root {
    --navy: #0355a3;
    --mid-blue: #3276b5;
    --bright-blue: #0393ce;
    --sky-blue: #34a6d7;
    --deep-navy: #173a78;
    --paper: #f4f5f6;
    --paper-shade: #e3e5e8;
    --ink-grey: #5a6470;
    --backdrop: #d9dbde;
  }
  * { box-sizing: border-box; margin: 0; padding: 0; }
  html, body {
    width: 1200px; height: 660px; overflow: hidden;
    background: var(--backdrop);
    font-family: "Source Sans 3", "Helvetica Neue", Arial, sans-serif;
  }
  .stage {
    position: relative; width: 1200px; height: 660px;
    display: flex; align-items: center; justify-content: center; gap: 40px;
  }
  .card {
    position: relative; width: 540px; height: 308px; overflow: hidden;
    box-shadow: 0 6px 18px rgba(0,0,0,0.18);
  }

  /* Front */
  .card-front {
    background: radial-gradient(ellipse at 70% 25%, var(--sky-blue) 0%, var(--bright-blue) 35%, var(--mid-blue) 70%, var(--navy) 100%);
    display: flex; flex-direction: column; align-items: center; justify-content: center;
  }
  .brand { display: flex; align-items: center; gap: 10px; }
  .brand-square { width: 14px; height: 14px; background: var(--deep-navy); }
  .front-name { color: #fff; font-size: 28px; font-weight: 600; letter-spacing: 0.2px; }
  .front-tagline { margin-top: 4px; color: var(--deep-navy); font-size: 12px; font-weight: 700; }

  /* Back */
  .card-back {
    background: linear-gradient(135deg, #fafbfb 0%, var(--paper) 55%, var(--paper-shade) 100%);
  }
  .person { position: absolute; top: 30px; right: 34px; text-align: right; }
  .person-name { font-size: 22px; color: var(--deep-navy); letter-spacing: 0.5px; }
  .person-name strong { font-weight: 700; }
  .person-title { font-size: 14px; color: var(--bright-blue); margin-top: -3px; }
  .edge-tab { position: absolute; top: 32px; right: 0; width: 10px; height: 24px; background: var(--sky-blue); }

  .back-brand { position: absolute; left: 40px; top: 118px; }
  .back-name { color: var(--bright-blue); font-size: 27px; font-weight: 400; }
  .back-tagline { color: var(--deep-navy); font-size: 12.5px; font-weight: 700; margin-top: 1px; }

  .contacts { position: absolute; left: 40px; top: 196px; list-style: none; }
  .contacts li { display: flex; align-items: center; gap: 9px; color: var(--ink-grey); font-size: 16px; line-height: 21px; }
  .contacts svg { width: 14px; height: 14px; flex: none; }
  .address { position: absolute; left: 40px; top: 262px; color: var(--ink-grey); font-size: 15px; line-height: 18px; }
  .edge-strip {
    position: absolute; left: 0; top: 190px; width: 12px; height: 118px;
    background: linear-gradient(180deg, var(--mid-blue), var(--navy));
  }
</style>
</head>
<body>
<main class="stage">
  <section class="card card-front" aria-label="Card front">
    <div class="brand">
      <span class="brand-square"></span>
      <span class="front-name">Vorna Electric Construction</span>
    </div>
    <p class="front-tagline">Certified DBE &amp; MWBE Electrical Contractor</p>
  </section>

  <section class="card card-back" aria-label="Card back">
    <div class="edge-tab"></div>
    <div class="person">
      <p class="person-name">YOUR <strong>NAME</strong></p>
      <p class="person-title">Title</p>
    </div>

    <div class="back-brand">
      <p class="back-name">Vorna Electric Construction</p>
      <p class="back-tagline">Certified DBE &amp; MWBE Electrical Contractor</p>
    </div>

    <div class="edge-strip"></div>
    <ul class="contacts">
      <li>
        <svg viewBox="0 0 14 14"><rect width="14" height="14" rx="2" fill="var(--navy)"/><path d="M4 3.5c.6 0 1 .9 1.2 1.5.1.4-.5.7-.6 1 .4 1 1.3 1.9 2.4 2.4.3-.1.6-.7 1-.6.6.2 1.5.6 1.5 1.2 0 .6-.7 1.5-1.4 1.5C5.6 10.5 3.5 8.4 3 5c0-.7.4-1.5 1-1.5z" fill="#fff"/></svg>
        <span>123-456-7890</span>
      </li>
      <li>
        <svg viewBox="0 0 14 14"><rect width="14" height="14" rx="2" fill="var(--navy)"/><rect x="3" y="4.5" width="8" height="5.5" fill="none" stroke="#fff" stroke-width="1"/><path d="M3 4.5l4 3 4-3" fill="none" stroke="#fff" stroke-width="1"/></svg>
        <span>yourname@vornaec.com</span>
      </li>
      <li>
        <svg viewBox="0 0 14 14"><circle cx="7" cy="7" r="7" fill="var(--bright-blue)"/><circle cx="7" cy="7" r="4" fill="none" stroke="#fff" stroke-width="1"/><path d="M3 7h8M7 3c-1.6 2.4-1.6 5.6 0 8M7 3c1.6 2.4 1.6 5.6 0 8" fill="none" stroke="#fff" stroke-width="0.8"/></svg>
        <span>www.vornaec.com</span>
      </li>
    </ul>
    <p class="address">company address, company address<br>company address</p>
  </section>
</main>
</body>
</html>
```